Wendell's UPDATE -Across the Board

Insurance Agent Business card and probably everything else !
Been in business for over 35 years and never took the time to update so really like the black-gold combo but open for suggestions (Honestly, I have NO idea how this works but sounds very cool ) Attached are two samples that I enjoy. The black and gold option is my favorite so looking for something like that!

```html
<!DOCTYPE html>
<html lang="en">
<head>
<meta charset="utf-8">
<title>Wendell S Harlow – Business Card</title>
<link href="https://fonts.googleapis.com/css2?family=Cinzel:wght@600&family=Montserrat:wght@300;400&display=swap" rel="stylesheet">
<style>
  :root {
    --page: #e9e6e1;
    --ink-black: #050505;
    --card-dark: #151515;
    --gold: #c9a25a;
    --gold-light: #efd48e;
    --gold-deep: #8a6a2c;
    --silver: #b9b9b9;
    --text-white: #f2f2f2;
  }
  * { margin: 0; padding: 0; box-sizing: border-box; }
  html, body {
    width: 1179px; height: 1200px; overflow: hidden;
    background: var(--page);
  }
  .sheet {
    width: 1179px; height: 1200px;
    display: flex; flex-direction: column; align-items: center; justify-content: center;
    gap: 32px;
  }
  .card {
    position: relative;
    width: 960px; height: 552px;
    background: var(--card-dark);
    overflow: hidden;
    box-shadow: 0 6px 18px rgba(0,0,0,0.25);
  }
  .card__waves { position: absolute; inset: 0; width: 100%; height: 100%; }

  .card__name {
    position: absolute; top: 40px; left: 0; width: 100%;
    text-align: center;
    font-family: "Cinzel", serif; font-weight: 600;
    font-size: 36px; letter-spacing: 1px;
    color: var(--gold);
  }
  .card__title {
    position: absolute; top: 88px; left: 0; width: 100%;
    text-align: center;
    font-family: "Montserrat", sans-serif; font-weight: 400;
    font-size: 19px; letter-spacing: 0.3px;
    color: var(--text-white);
  }
  .brand {
    position: absolute;
    font-family: "Cinzel", serif; font-weight: 600;
    color: var(--gold);
    text-align: center;
  }
  .brand--front { left: 230px; top: 360px; width: 190px; font-size: 40px; letter-spacing: 10px; }
  .brand--back { left: 0; top: 150px; width: 100%; font-size: 84px; letter-spacing: 22px; }

  .contacts {
    position: absolute; left: 440px; top: 330px;
    list-style: none;
    font-family: "Montserrat", sans-serif; font-weight: 300;
    font-size: 21px; color: var(--text-white);
  }
  .contacts__item { display: flex; align-items: center; height: 30px; margin-bottom: 19px; }
  .contacts__icon {
    width: 31px; height: 31px; margin-right: 20px;
    background: var(--gold-light);
    display: flex; align-items: center; justify-content: center;
  }
  .contacts__icon svg { width: 19px; height: 19px; }

  .address {
    position: absolute; left: 0; top: 432px; width: 100%;
    text-align: center;
    font-family: "Montserrat", sans-serif; font-weight: 400;
    font-size: 21px; line-height: 34px;
    color: var(--text-white);
  }
</style>
</head>
<body>
<main class="sheet">

  <section class="card card--front" aria-label="Card front">
    <svg class="card__waves" viewBox="0 0 960 552" aria-hidden="true">
      <defs>
        <linearGradient id="goldBand" x1="0" x2="1" y1="0" y2="0">
          <stop offset="0" stop-color="#9c7a3a"/>
          <stop offset="0.3" stop-color="#efd48e"/>
          <stop offset="0.55" stop-color="#b58d46"/>
          <stop offset="1" stop-color="#d8b66e"/>
        </linearGradient>
        <linearGradient id="silverBand" x1="0" x2="1" y1="0" y2="0">
          <stop offset="0" stop-color="#3a3a3a"/>
          <stop offset="0.45" stop-color="#e4e4e4"/>
          <stop offset="0.75" stop-color="#6e6e6e"/>
          <stop offset="1" stop-color="#c8c8c8"/>
        </linearGradient>
      </defs>
      <path d="M0,0 H960 V160 C800,120 660,120 520,145 C380,170 200,178 0,172 Z" fill="var(--ink-black)"/>
      <path d="M360,165 C520,110 720,100 960,165 L960,200 C760,145 560,150 420,195 Z" fill="url(#silverBand)"/>
      <path d="M0,172 C200,178 380,172 520,148 C680,122 820,128 960,172 L960,186 C800,152 660,158 520,182 C360,212 200,240 0,238 Z" fill="url(#goldBand)"/>
    </svg>

    <h1 class="card__name">Wendell S Harlow</h1>
    <p class="card__title">INSURANCE &amp; FINANCIAL CONSULTANT</p>

    <div class="brand brand--front">WSH</div>

    <ul class="contacts">
      <li class="contacts__item">
        <span class="contacts__icon">
          <svg viewBox="0 0 24 24"><path d="M6.6 10.8c1.4 2.8 3.8 5.1 6.6 6.6l2.2-2.2c.3-.3.7-.4 1-.2 1.1.4 2.3.6 3.6.6.6 0 1 .4 1 1V20c0 .6-.4 1-1 1C10.6 21 3 13.4 3 4c0-.6.4-1 1-1h3.5c.6 0 1 .4 1 1 0 1.3.2 2.5.6 3.6.1.3 0 .7-.2 1z" fill="#1a1a1a"/></svg>
        </span>954-555-0142
      </li>
      <li class="contacts__item">
        <span class="contacts__icon">
          <svg viewBox="0 0 24 24"><rect x="4" y="9" width="16" height="11" fill="#1a1a1a"/><rect x="7" y="3" width="10" height="6" fill="none" stroke="#1a1a1a" stroke-width="2"/><rect x="7" y="12" width="3" height="2" fill="#efd48e"/><rect x="12" y="12" width="5" height="2" fill="#efd48e"/></svg>
        </span>954-555-0187
      </li>
      <li class="contacts__item">
        <span class="contacts__icon">
          <svg viewBox="0 0 24 24"><rect x="3" y="6" width="18" height="12" fill="#1a1a1a"/><path d="M3 6l9 7 9-7" fill="none" stroke="#efd48e" stroke-width="1.5"/></svg>
        </span>wendell@wshinsures.com
      </li>
    </ul>
  </section>

  <section class="card card--back" aria-label="Card back">
    <svg class="card__waves" viewBox="0 0 960 552" aria-hidden="true">
      <defs>
        <linearGradient id="goldBandBack" x1="0" x2="1" y1="0" y2="0">
          <stop offset="0" stop-color="#8a6a2c"/>
          <stop offset="0.5" stop-color="#c9a25a"/>
          <stop offset="0.8" stop-color="#efd48e"/>
          <stop offset="1" stop-color="#b58d46"/>
        </linearGradient>
        <linearGradient id="silverBandBack" x1="0" x2="1" y1="0" y2="0">
          <stop offset="0" stop-color="#4a4a4a"/>
          <stop offset="0.25" stop-color="#d8d8d8"/>
          <stop offset="0.6" stop-color="#5a5a5a"/>
          <stop offset="1" stop-color="#2a2a2a"/>
        </linearGradient>
      </defs>
      <path d="M0,360 C180,330 360,395 520,380 C700,360 820,330 960,330 V552 H0 Z" fill="var(--ink-black)"/>
      <path d="M0,340 C150,318 300,350 430,365 C540,378 600,372 660,360 L640,385 C560,400 460,395 360,380 C220,358 100,350 0,368 Z" fill="url(#silverBandBack)"/>
      <path d="M0,352 C180,380 360,395 520,370 C680,340 820,320 960,310 L960,365 C820,355 700,360 560,385 C420,405 220,395 0,358 Z" fill="url(#goldBandBack)"/>
    </svg>

    <div class="brand brand--back">WSH</div>

    <p class="address">4120 Palmetto Avenue, Suite 310<br>Linden Park, FL 33099</p>
  </section>

</main>
</body>
</html>
```